KORBALT

The business want a professional looking business card. We have a scetch we will add but want the extra upgrade, and would like more suggestions for variations of our business cards.

```html
<!DOCTYPE html>
<html lang="en">
<head>
<meta charset="utf-8">
<title>KORBALT – Business Card</title>
<link href="https://fonts.googleapis.com/css2?family=Federo&family=Nunito:wght@300;400&display=swap" rel="stylesheet">
<style>
  :root {
    --stage: #1c1a19;
    --card: #ffffff;
    --gold: #eda23a;
    --grey: #9d9d9d;
  }
  * { margin: 0; padding: 0; box-sizing: border-box; }
  html, body {
    width: 1006px;
    height: 1200px;
    overflow: hidden;
    background: var(--stage);
  }
  .card {
    position: absolute;
    left: 30px;
    top: 335px;
    width: 946px;
    height: 530px;
    background: var(--card);
  }
  .brand {
    position: absolute;
    left: 47px;
    top: 70px;
    width: 300px;
    text-align: center;
  }
  .brand-dot {
    display: block;
    width: 96px;
    height: 96px;
    margin: 0 auto 34px;
    border-radius: 50%;
    background: var(--gold);
  }
  .brand-name {
    font-family: "Federo", sans-serif;
    font-size: 36px;
    letter-spacing: 0.32em;
    margin-right: -0.32em;
    color: var(--gold);
  }
  .details {
    position: absolute;
    left: 484px;
    top: 258px;
  }
  .details-name {
    font-family: "Federo", sans-serif;
    font-size: 40px;
    line-height: 1;
    color: var(--gold);
    letter-spacing: 0.01em;
  }
  .details-role {
    font-family: "Nunito", sans-serif;
    font-weight: 300;
    font-size: 34px;
    line-height: 1;
    color: var(--grey);
    margin-top: 10px;
  }
  .details-person {
    font-family: "Nunito", sans-serif;
    font-size: 19px;
    color: var(--grey);
    margin-top: 2px;
  }
  .contacts {
    list-style: none;
    margin-top: 26px;
  }
  .contact {
    display: flex;
    align-items: center;
    height: 34px;
    font-family: "Nunito", sans-serif;
    font-weight: 300;
    font-size: 24px;
    color: var(--grey);
    letter-spacing: 0.02em;
  }
  .contact svg {
    width: 22px;
    height: 22px;
    margin-right: 20px;
    flex: none;
  }
</style>
</head>
<body>
  <main class="card">
    <div class="brand">
      <span class="brand-dot"></span>
      <div class="brand-name">KORBALT</div>
    </div>

    <section class="details">
      <h1 class="details-name">KORBALT SOLVANG</h1>
      <p class="details-role">CEO &amp; Founder</p>
      <p class="details-person">Lars Henrik Solvang</p>
      <ul class="contacts">
        <li class="contact">
          <svg viewBox="0 0 22 22" aria-hidden="true">
            <rect x="5" y="1" width="12" height="20" rx="2" fill="none" stroke="#eda23a" stroke-width="2"/>
            <circle cx="11" cy="17.5" r="1.2" fill="#eda23a"/>
          </svg>
          004791234567
        </li>
        <li class="contact">
          <svg viewBox="0 0 22 22" aria-hidden="true">
            <rect x="1" y="5" width="20" height="13" fill="#eda23a"/>
            <path d="M1 5 L11 12.5 L21 5" fill="none" stroke="#fff" stroke-width="1.5"/>
          </svg>
          korbalt.llc@mailbox.com
        </li>
        <li class="contact">
          <svg viewBox="0 0 22 22" aria-hidden="true">
            <g fill="none" stroke="#eda23a" stroke-width="1.6">
              <circle cx="11" cy="11" r="9.5"/>
              <ellipse cx="11" cy="11" rx="4.5" ry="9.5"/>
              <path d="M1.5 11 H20.5 M3 6 H19 M3 16 H19"/>
            </g>
          </svg>
          www.korbalt.llc
        </li>
      </ul>
    </section>
  </main>
</body>
</html>
```